Marlow Brochure

Brevik & Solan Education Group was formed in 2011 as an organizational arm
to put educational and charitable services together for community
development.

B & S was acquired by Marlow Education Group in 2013 and relocated to Texas
with the expressed focus of reaching underserved communities and
population, both in the Dallas- Fort Worth Metropolitan area and Houston
areas. Key members of the organization are based in Dallas, TX, Houston,
TX, Atlanta GA, and Washington DC and are strategically networked to
utilize their external resources for education advancement with
under-served populations.

Target Market(s)

- -The target market is 17-45 year olds, the demographics are 70%
women, 30% men, interested in an entry level education in
the health field

Industry/Entity Type

Education

```html
<!DOCTYPE html>
<html lang="en">
<head>
<meta charset="utf-8">
<title>Marlow Brochure</title>
<link href="https://fonts.googleapis.com/css2?family=PT+Sans:ital,wght@0,400;0,700;1,700&family=Open+Sans:wght@600;700&display=swap" rel="stylesheet">
<style>
  :root {
    --leaf: #8cc63f;
    --leaf-deep: #7dbb2e;
    --leaf-light: #b5da6e;
    --white: #ffffff;
    --brand-blue: #2f6fc0;
    --brand-green: #1f8f3a;
    --url-blue: #1f6db5;
    --fold: #333333;
    --photo-sky: #4a7fc6;
    --photo-field: #7fae3c;
    --photo-soil: #5b3c28;
  }
  html, body { margin: 0; padding: 0; overflow: hidden; background: var(--white); }
  .brochure {
    position: relative;
    width: 1200px;
    height: 900px;
    overflow: hidden;
    background: linear-gradient(180deg, var(--leaf) 0%, var(--leaf-deep) 45%, var(--leaf-light) 100%);
    font-family: "PT Sans", Arial, sans-serif;
    color: var(--white);
  }
  .backdrop { position: absolute; inset: 0; }
  .fold {
    position: absolute; top: 0; bottom: 0; width: 0;
    border-left: 1.5px dashed var(--fold);
  }
  .fold--one { left: 390px; }
  .fold--two { left: 797px; }

  .panel { position: absolute; top: 0; height: 900px; }
  .panel--history { left: 0; width: 390px; }
  .panel--inside { left: 390px; width: 407px; text-align: center; }
  .panel--cover { left: 797px; width: 403px; text-align: center; }

  .history__title {
    position: absolute; left: 34px; top: 84px; margin: 0;
    font-size: 33px; font-weight: 700; letter-spacing: 0.5px;
  }
  .history__body {
    position: absolute; left: 34px; top: 130px; width: 322px; margin: 0;
    font-size: 16px; line-height: 25px;
  }
  .photo {
    position: absolute; border: 5px solid var(--white);
    box-shadow: 3px 4px 8px rgba(0,0,0,0.35);
  }
  .photo--sunflower {
    left: 28px; top: 566px; width: 138px; height: 95px; transform: rotate(2deg);
    background: var(--photo-sky);
  }
  .photo--terraces {
    left: 199px; top: 560px; width: 136px; height: 96px; transform: rotate(-2deg);
    background: var(--photo-field);
  }
  .photo--seedling {
    left: 104px; top: 670px; width: 168px; height: 120px; transform: rotate(-9deg);
    background: var(--photo-soil);
  }

  .inside__headline {
    position: absolute; left: 0; right: 0; top: 284px; margin: 0;
    font-size: 28px; font-weight: 700; line-height: 40px;
  }
  .mark {
    position: absolute; left: 0; right: 0;
    display: flex; align-items: center; justify-content: center; gap: 10px;
    font-family: "PT Sans", Arial, sans-serif; font-weight: 400; color: var(--brand-blue);
  }
  .mark__dot { border-radius: 50%; background: var(--brand-blue); }
  .mark--inside { top: 732px; font-size: 20px; }
  .mark--inside .mark__dot { width: 14px; height: 14px; }
  .inside__tagline {
    position: absolute; left: 0; right: 0; top: 792px; margin: 0;
    font-size: 21px; font-weight: 700;
  }

  .cover__title {
    position: absolute; left: 0; right: 0; top: 50px; margin: 0;
    font-family: "Open Sans", Arial, sans-serif; font-weight: 600;
    font-size: 63px; line-height: 87px;
  }
  .cover__title-line { display: block; }
  .cover__title-line--blue { color: var(--brand-blue); }
  .cover__title-line--green { color: var(--brand-green); }
  .mark--cover { top: 430px; font-size: 30px; }
  .mark--cover .mark__dot { width: 22px; height: 22px; }
  .cover__promise {
    position: absolute; left: 0; right: 0; top: 632px; margin: 0;
    font-size: 35px; font-weight: 700; font-style: italic; line-height: 51px;
  }
  .cover__url {
    position: absolute; left: 0; right: 0; top: 860px; margin: 0;
    font-size: 23px; font-weight: 700; color: var(--url-blue); letter-spacing: 0.3px;
  }
</style>
</head>
<body>
<main class="brochure">
  <svg class="backdrop" width="1200" height="900" viewBox="0 0 1200 900" aria-hidden="true">
    <polygon points="0,360 1200,250 1200,330 0,470" fill="#9dce52" opacity="0.55"/>
    <polygon points="0,500 1200,400 1200,520 0,640" fill="#a6d45e" opacity="0.6"/>
    <polygon points="0,640 1200,560 1200,700 0,770" fill="#b9de78" opacity="0.6"/>
    <polygon points="0,760 1200,720 1200,810 0,830" fill="#c8e58e" opacity="0.7"/>
    <path d="M0,0 H1200 V20 C1000,40 820,30 797,28 C700,40 560,80 390,72 C260,55 120,30 0,45 Z" fill="#ffffff"/>
    <path d="M390,72 C520,90 680,60 797,30 L797,50 C680,85 520,110 390,95 Z" fill="#d9efb3" opacity="0.8"/>
    <path d="M0,830 C300,845 700,860 1200,835 V900 H0 Z" fill="#e6f3cf"/>
    <path d="M0,850 C400,870 800,880 1200,850 V900 H0 Z" fill="#ffffff"/>
  </svg>

  <div class="fold fold--one"></div>
  <div class="fold fold--two"></div>

  <section class="panel panel--history">
    <h2 class="history__title">History</h2>
    <p class="history__body">Brevik &amp; Solan Education Group was formed in 2011 as an organizational arm to put educational and charitable services together for community development.<br>B &amp; S was acquired by Marlow Education Group in 2013 and relocated to Texas with the expressed focus of reaching under-served communities and population, both in the Dallas- Fort Worth Metropolitan area and Houston areas. Key members of the organization are based in Dallas, TX, Houston, TX, Atlanta GA, and Washington DC and are strategically networked to utilize their external resources for education advance-ment with under-served populations.</p>
    <div class="photo photo--sunflower" role="img" aria-label="Photo of a sunflower against a blue sky"></div>
    <div class="photo photo--terraces" role="img" aria-label="Photo of green terraced farm fields"></div>
    <div class="photo photo--seedling" role="img" aria-label="Photo of hands holding soil with a young seedling"></div>
  </section>

  <section class="panel panel--inside">
    <h2 class="inside__headline">Training at work for<br>you</h2>
    <div class="mark mark--inside"><span class="mark__dot"></span><span>Marlow Education Group</span></div>
    <p class="inside__tagline">On track to your Purpose</p>
  </section>

  <section class="panel panel--cover">
    <h1 class="cover__title">
      <span class="cover__title-line cover__title-line--blue">Marlow</span>
      <span class="cover__title-line cover__title-line--green">Education</span>
      <span class="cover__title-line cover__title-line--blue">Group</span>
    </h1>
    <div class="mark mark--cover"><span class="mark__dot"></span><span>Marlow</span></div>
    <p class="cover__promise">Connecting Your<br>Training To Your<br>Purpose…</p>
    <p class="cover__url">www.MarlowEd.com</p>
  </section>
</main>
</body>
</html>
```